Liquor Label / Aguardiente

Label design for liquor bottle. Designers may submit multiple submissions.

Product Description:
Name: Viento de Plata™
Alcohol Category: Aguardiente (which in Spanish most closely translates to “burning water”) – aguardiente is derived from
cane sugar and is a general term for a type of alcoholic spirit in many Central and South America countries.
Taste: A smooth liquor with a comfortable yet spicy finish
Smell: Subtle aroma of spicy jalapeños
Liquid Color: Clear
Bottle Color: Clear
See link for reference - http://www.kelvostamp.com/sites/default/files/styles/uc_product_full/public/Pemrow_0.jpg?itok=9QmT2xLp
Closure: Bar top / cork
Bottle Shape/Size: height = 8.67in; diameter of base = 3.70in; diameter of neck = 0.85in

Label may consist of two separate parts (i.e. front and back, front and vertical side), or one continuous label.

Designer has complete freedom with color, font etc. unless otherwise stated below. The label MUST
contain (but is not limited only to) the following text exactly as written in quotes below:
- “Viento de Plata”
- “Aguardiente”
- “Cane Neutral Spirit with Natural Flavors”
- “35% Alc./Vol.”
- “750 ml”
- “Bottled by WP Spirits, LLC” and “Nashville, TN” - “Government Warning: (1) According to the Surgeon General, women should not drink alcoholic beverages during
pregnancy because of the risk of birth defects. (2) Consumption of alcoholic beverages impairs your ability to
drive a car or operate machinery, and may cause health problems.” (text in previous quotes must be in all
capitalized letters, text must be 2 MM in height and quote must be separated 2MM by all other text)
- Must be dedicated empty space for bar code (approximately 0.75in. height x 1.25in. length)

Target Market(s)

Label should have mass market appeal.
Age: 21 – 28 years old (primary target market is 21+ year old college students and recent graduates)
Target Market Gender: Both male and female, with emphasis on male
Consumption Focus: Spirit will be consumed typically as a shot, primarily at bars and secondarily off premise (label design will be critical for making our product highly visible behind a bar)
Marketing Theme: South American elements. The official Viento de Plata mascot is a llama and the incorporation and use of a llama somewhere (however large or small) on the bottle is encourage but by no means required.

Industry/Entity Type

Health

Requirements
Should not have
• Elements that may lead a potential consumer to believe the beverage is a craft liquor or an artisan brand. Please do not include images of peppers.

```html
<!DOCTYPE html>
<html lang="en">
<head>
<meta charset="utf-8">
<title>Viento de Plata – Aguardiente Label</title>
<link rel="stylesheet" href="https://fonts.googleapis.com/css2?family=Roboto+Slab:wght@700;900&family=Cinzel:wght@500&display=swap">
<style>
  :root {
    --backdrop: #0b0b0b;
    --label-frame: #0d0d0d;
    --label-trim: #b8962e;
    --flame-deep: #b8431a;
    --flame-mid: #e98a2c;
    --flame-light: #f6c96a;
    --field-gold: #f3d34a;
    --field-pale: #f8e58a;
    --title-ink: #fbf4ea;
    --wine: #7a1616;
    --ink: #1a1a1a;
    --code-space: #ffffff;
  }
  * { margin: 0; padding: 0; box-sizing: border-box; }
  html, body {
    width: 1200px; height: 900px; overflow: hidden;
    background: var(--backdrop);
  }
  .canvas {
    position: relative; width: 1200px; height: 900px;
    display: flex; align-items: center; justify-content: center;
  }
  .label {
    position: relative; width: 450px; height: 820px;
    border-radius: 56px;
    border: 3px solid var(--label-trim);
    padding: 12px;
    background: var(--backdrop);
  }
  .label-frame {
    position: relative; width: 100%; height: 100%;
    border-radius: 46px;
    background: var(--label-frame);
    padding: 14px;
  }
  .label-field {
    position: relative; width: 100%; height: 100%;
    border-radius: 34px; overflow: hidden;
    background: linear-gradient(180deg, var(--field-pale) 0%, var(--field-gold) 100%);
    text-align: center;
  }
  .flame-swirl {
    position: absolute; left: 0; top: 0; width: 100%; height: 62%;
    background:
      radial-gradient(ellipse at 30% 35%, var(--flame-light) 0%, transparent 55%),
      linear-gradient(180deg, var(--flame-deep) 0%, var(--flame-mid) 55%, var(--field-gold) 100%);
  }
  .label-content {
    position: relative; z-index: 1;
    display: flex; flex-direction: column; align-items: center;
    height: 100%; padding: 40px 22px 0;
  }
  .brand-name {
    font-family: 'Roboto Slab', serif; font-weight: 900;
    color: var(--title-ink);
    font-size: 80px; line-height: 0.98; letter-spacing: 1px;
    text-transform: uppercase;
  }
  .category {
    margin-top: 22px;
    font-family: 'Cinzel', serif; font-weight: 500;
    color: var(--wine); font-size: 36px; letter-spacing: 2px;
    line-height: 1.1;
  }
  .divider {
    margin-top: 14px; width: 100%; height: 2px; background: var(--ink);
  }
  .spirit-type {
    margin-top: 16px;
    font-family: 'Roboto Slab', serif; font-weight: 700;
    color: var(--ink); font-size: 23px; line-height: 1.25;
  }
  .bottler {
    margin-top: 16px;
    font-family: 'Roboto Slab', serif; font-weight: 700;
    color: var(--ink); font-size: 13px; line-height: 1.35;
  }
  .volume {
    margin-top: 10px; width: 100%;
    display: flex; justify-content: space-between;
    font-family: 'Roboto Slab', serif; font-weight: 700;
    color: var(--ink); font-size: 15px; line-height: 1.2;
  }
  .label-footer {
    margin-top: 12px; width: 100%;
    display: flex; align-items: flex-start; gap: 12px;
  }
  .gov-warning {
    flex: 1;
    font-family: 'Roboto Slab', serif; font-weight: 700;
    color: var(--ink); font-size: 8.6px; line-height: 1.3;
    text-align: left; text-transform: uppercase;
  }
  .code-space {
    flex: none; width: 112px; height: 68px;
    background: var(--code-space);
    border: 1px solid var(--ink);
  }
</style>
</head>
<body>
  <main class="canvas">
    <article class="label">
      <div class="label-frame">
        <div class="label-field">
          <div class="flame-swirl" role="img" aria-label="Swirling flame texture in orange and gold"></div>
          <div class="label-content">
            <h1 class="brand-name">Viento<br>de<br>Plata</h1>
            <p class="category">AGUARDIENTE</p>
            <div class="divider"></div>
            <p class="spirit-type">Cane Neutral Spirit<br>with Natural Flavors</p>
            <p class="bottler">Bottled by WP Spirits, LLC<br>Nashville, TN</p>
            <div class="volume"><span>35% Alc./Vol.</span><span>750 ml</span></div>
            <div class="label-footer">
              <p class="gov-warning">Government Warning: (1) According to the Surgeon General, women should not drink alcoholic beverages during pregnancy because of the risk of birth defects. (2) Consumption of alcoholic beverages impairs your ability to drive a car or operate machinery, and may cause health problems.</p>
              <div class="code-space" aria-label="Reserved space for bar code"></div>
            </div>
          </div>
        </div>
      </div>
    </article>
  </main>
</body>
</html>
```